I need a business card that is professional /minimalistic ( clean edges) to help develop my new business venture that is car valeting / detailing.

I would like to use a black background, white font,red car silhouette above the text.
Updates

have now added phone numbers thanks

Industry/Entity Type

Business

Contact Information for Business Card

Gleamcraft Studio,
Valeting & Detailing Specialist,
tel 01632 960418 mob 07700 900583, Dale Hextor, 7 Marlow Rise. West Fenby, Beccles. NR91 3XQ

```html
<!DOCTYPE html>
<html lang="en">
<head>
<meta charset="utf-8">
<title>Gleamcraft Studio – Business Card</title>
<link href="https://fonts.googleapis.com/css2?family=Questrial&display=swap" rel="stylesheet">
<style>
  :root {
    --page-bg: #e6e4e1;
    --card-black: #231f20;
    --band-grey: #3e3e40;
    --text-white: #f2f2f2;
    --accent-red: #e01b1b;
    --shadow: rgba(0, 0, 0, 0.28);
  }

  html, body {
    margin: 0;
    padding: 0;
    width: 1200px;
    height: 900px;
    overflow: hidden;
    background: var(--page-bg);
  }

  .canvas {
    position: relative;
    width: 1200px;
    height: 900px;
  }

  .business-card {
    position: absolute;
    left: 100px;
    top: 130px;
    width: 1000px;
    height: 640px;
    background: var(--card-black);
    box-shadow: 0 14px 36px var(--shadow);
    font-family: "Questrial", "Century Gothic", sans-serif;
    color: var(--text-white);
    overflow: hidden;
  }

  .car-emblem-area {
    position: absolute;
    left: 270px;
    top: 185px;
    width: 460px;
    height: 100px;
    background: radial-gradient(ellipse at center, var(--accent-red) 0%, rgba(224, 27, 27, 0.55) 45%, rgba(35, 31, 32, 0) 72%);
  }

  .tagline {
    position: absolute;
    left: 0;
    right: 0;
    top: 312px;
    margin: 0;
    text-align: center;
    font-size: 40px;
    font-weight: 400;
    letter-spacing: 0.2px;
  }

  .contact-band {
    position: absolute;
    left: 0;
    right: 0;
    bottom: 0;
    height: 170px;
    background: var(--band-grey);
  }

  .phone-list {
    position: absolute;
    left: 160px;
    top: 38px;
    margin: 0;
    padding: 0;
    list-style: none;
  }

  .phone-item {
    display: flex;
    align-items: center;
    height: 44px;
    font-size: 26px;
  }

  .phone-icon {
    width: 28px;
    height: 28px;
    margin-right: 28px;
    fill: var(--text-white);
  }

  .band-divider {
    position: absolute;
    left: 445px;
    top: 44px;
    width: 4px;
    height: 82px;
    background: var(--text-white);
  }

  .postal-address {
    position: absolute;
    left: 495px;
    top: 44px;
    font-style: normal;
    font-size: 22px;
    line-height: 28px;
  }
</style>
</head>
<body>
<main class="canvas">
  <article class="business-card">
    <div class="car-emblem-area" role="img" aria-label="Red sports car silhouette emblem"></div>

    <h1 class="tagline">Gleamcraft Studio, Valeting &amp; Detailing Specialist</h1>

    <footer class="contact-band">
      <ul class="phone-list">
        <li class="phone-item">
          <svg class="phone-icon" viewBox="0 0 28 28" aria-label="Telephone">
            <path d="M2 10 C2 5 26 5 26 10 L26 12 L20 12 L19 9 C16 8 12 8 9 9 L8 12 L2 12 Z"/>
            <path d="M7 13 L10 11 L18 11 L21 13 L23 24 L5 24 Z"/>
            <circle cx="14" cy="17.5" r="3.2" fill="var(--band-grey)"/>
          </svg>
          <span>01632 960418</span>
        </li>
        <li class="phone-item">
          <svg class="phone-icon" viewBox="0 0 28 28" aria-label="Mobile">
            <rect x="8" y="2" width="13" height="24" rx="2.5"/>
            <rect x="10" y="5" width="9" height="15" fill="var(--band-grey)"/>
            <circle cx="14.5" cy="23" r="1.3" fill="var(--band-grey)"/>
          </svg>
          <span>07700 900583</span>
        </li>
      </ul>

      <div class="band-divider"></div>

      <address class="postal-address">
        Dale Hextor, 7 Marlow Rise.<br>
        West Fenby, Beccles.<br>
        NR91 3XQ
      </address>
    </footer>
  </article>
</main>
</body>
</html>
```